Dr. Marissa Tevlin Medical/Chiropractic Business Card

Dr. Tevlin is a chiropractor and will require a business card that she uses every single day to book appointments on the back side of the card. Currently the office name goes by Dr. Marissa Tevlin. The chiropractic profession is based on the diagnosis and manipulative treatment of misalignments of the joints, especially those of the spinal column, which are held to cause other disorders by affecting the nerves, muscles, and organs. Dr. Marissa Tevlin is looking for a contemporary and minimalistic design.

Industry/Entity Type

Medical

Contact Information for Business Card

Name: Dr. Marissa Tevlin; Address: 748 Harcastle Rd South, London, ON N5R 2K7; Phone Number: 519.274.6193; Fax: 519.281.5046; email: marissa.tevlin@quorvamail.com

Requirements
Must have
• ability to write multiple appointments date/time on the back of card

```html
<!DOCTYPE html>
<html lang="en">
<head>
<meta charset="utf-8">
<title>Dr. Marissa Tevlin – Chiropractor Business Card</title>
<link href="https://fonts.googleapis.com/css2?family=Arimo:wght@400;700&display=swap" rel="stylesheet">
<style>
  :root {
    --navy: #2e2f86;
    --navy-deep: #24256e;
    --navy-light: #4a4fa6;
    --violet: #5a5cb0;
    --paper: #ffffff;
    --ink: #1d1d1d;
    --stage: #e9e8ec;
  }
  * { box-sizing: border-box; margin: 0; padding: 0; }
  html, body { width: 1200px; height: 900px; overflow: hidden; }
  body {
    background: var(--stage);
    font-family: "Arimo", Arial, sans-serif;
    position: relative;
  }
  .card {
    position: absolute;
    background: var(--paper);
    box-shadow: 0 6px 18px rgba(0,0,0,0.18);
    overflow: hidden;
  }

  /* Front */
  .card-front { left: 60px; top: 270px; width: 630px; height: 360px; }
  .front-identity {
    position: absolute; left: 0; top: 0; width: 100%; height: 185px;
    display: flex; align-items: center; padding-left: 110px; gap: 18px;
  }
  .identity-dot { width: 22px; height: 22px; border-radius: 50%; background: var(--navy); flex: none; }
  .identity-name { font-weight: 700; font-size: 40px; color: var(--navy); line-height: 1; }
  .identity-role { font-size: 24px; color: var(--violet); margin-top: 6px; }
  .front-rule { position: absolute; left: 0; width: 100%; background: var(--navy); }
  .front-rule.top { top: 185px; height: 7px; }
  .front-panel {
    position: absolute; left: 0; top: 198px; width: 100%; height: 120px;
    background: linear-gradient(180deg, var(--navy-light) 0%, var(--navy) 55%, var(--navy-deep) 100%);
    display: flex; align-items: center; color: var(--paper);
  }
  .front-address {
    width: 320px; text-align: right; padding-right: 18px; font-size: 15px; line-height: 1.45;
  }
  .front-divider { width: 1px; height: 70px; background: rgba(255,255,255,0.55); }
  .front-contacts { list-style: none; padding-left: 18px; font-size: 15px; line-height: 1.5; }
  .front-contacts li { display: flex; align-items: center; gap: 8px; }
  .front-contacts svg { width: 14px; height: 14px; flex: none; }
  .front-rule.bottom { top: 322px; height: 38px; background: var(--navy); }

  /* Back */
  .card-back { left: 770px; top: 120px; width: 370px; height: 650px; }
  .back-tab {
    position: absolute; left: 40px; top: 0; right: 0; height: 54px;
    background: linear-gradient(180deg, var(--navy-light), var(--navy-deep));
    border-top-right-radius: 18px;
    color: var(--paper); font-weight: 700; font-size: 20px; letter-spacing: 0.5px;
    display: flex; align-items: center; padding-left: 24px;
  }
  .appointment-list { position: absolute; left: 24px; right: 24px; top: 84px; list-style: none; }
  .appointment-row {
    display: flex; align-items: flex-end; gap: 8px; height: 45px;
    font-size: 18px; color: var(--ink);
  }
  .appointment-row .blank { border-bottom: 1.5px solid var(--ink); height: 1px; }
  .appointment-row .blank.date { flex: 1.4; }
  .appointment-row .blank.time { flex: 1; }
  .appointment-row .at { line-height: 1; transform: translateY(4px); }
  .back-note {
    position: absolute; left: 10px; right: 10px; bottom: 46px;
    text-align: center; color: var(--navy-deep); font-weight: 700; font-size: 16px; line-height: 1.3;
  }
</style>
</head>
<body>

<section class="card card-front" aria-label="Business card front">
  <div class="front-identity">
    <span class="identity-dot" aria-hidden="true"></span>
    <div>
      <div class="identity-name">Dr. Marissa Tevlin</div>
      <div class="identity-role">Chiropractor</div>
    </div>
  </div>
  <div class="front-rule top"></div>
  <div class="front-panel">
    <address class="front-address" style="font-style:normal">
      748 Harcastle Rd South, London<br>ON N5R 2K7
    </address>
    <span class="front-divider"></span>
    <ul class="front-contacts">
      <li>
        <svg viewBox="0 0 16 16" aria-label="Phone"><path fill="#fff" d="M3 1h3l1.5 4-2 1.2a9 9 0 0 0 4.3 4.3L11 8.5l4 1.5v3a2 2 0 0 1-2 2A12 12 0 0 1 1 3a2 2 0 0 1 2-2z"/></svg>
        519.274.6193
      </li>
      <li>
        <svg viewBox="0 0 16 16" aria-label="Fax"><rect x="4" y="1" width="8" height="5" fill="#fff"/><rect x="1" y="6" width="14" height="7" rx="1" fill="#fff"/><rect x="4" y="10" width="8" height="5" fill="#fff" stroke="#2e2f86" stroke-width="1"/></svg>
        519.281.5046
      </li>
      <li>
        <svg viewBox="0 0 16 16" aria-label="Email"><rect x="1" y="3" width="14" height="10" fill="#fff"/><path d="M1 3l7 5 7-5M1 13l5-5M15 13l-5-5" stroke="#2e2f86" stroke-width="1.3" fill="none"/></svg>
        marissa.tevlin@quorvamail.com
      </li>
    </ul>
  </div>
  <div class="front-rule bottom"></div>
</section>

<section class="card card-back" aria-label="Business card back">
  <div class="back-tab">APPOINTMENTS</div>
  <ol class="appointment-list">
    <li class="appointment-row"><span class="blank date"></span><span class="at">@</span><span class="blank time"></span></li>
    <li class="appointment-row"><span class="blank date"></span><span class="at">@</span><span class="blank time"></span></li>
    <li class="appointment-row"><span class="blank date"></span><span class="at">@</span><span class="blank time"></span></li>
    <li class="appointment-row"><span class="blank date"></span><span class="at">@</span><span class="blank time"></span></li>
    <li class="appointment-row"><span class="blank date"></span><span class="at">@</span><span class="blank time"></span></li>
    <li class="appointment-row"><span class="blank date"></span><span class="at">@</span><span class="blank time"></span></li>
    <li class="appointment-row"><span class="blank date"></span><span class="at">@</span><span class="blank time"></span></li>
    <li class="appointment-row"><span class="blank date"></span><span class="at">@</span><span class="blank time"></span></li>
    <li class="appointment-row"><span class="blank date"></span><span class="at">@</span><span class="blank time"></span></li>
    <li class="appointment-row"><span class="blank date"></span><span class="at">@</span><span class="blank time"></span></li>
  </ol>
  <p class="back-note">If you are unable to make your appointment,<br>please call us to reschedule</p>
</section>

</body>
</html>
```